Letter Head / Envelopes
Business Card
Professional
Glen Hartwick Sr
Managing Partner
418 Tamsin Rd Ashbury, PA 19377
glen@copperfieldre.com
www.copperfieldre.com

```html
<!DOCTYPE html>
<html lang="en">
<head>
<meta charset="utf-8">
<title>Copperfield Real Estate – Stationery</title>
<link href="https://fonts.googleapis.com/css2?family=Open+Sans:wght@400;600;700&display=swap" rel="stylesheet">
<style>
  :root{
    --navy:#1c2f6b;
    --gold:#f0b323;
    --gold-deep:#d9950f;
    --gold-light:#f9d46a;
    --paper:#ffffff;
    --ink:#333a48;
    --faint:#e3e6ee;
    --bg:#ece9e4;
  }
  *{box-sizing:border-box;margin:0;padding:0}
  html,body{width:1200px;height:742px;overflow:hidden}
  body{background:var(--bg);font-family:"Open Sans",Arial,sans-serif;color:var(--ink);position:relative}

  .sheet{position:absolute;background:var(--paper);box-shadow:0 3px 10px rgba(0,0,0,.18)}
  address{font-style:normal}

  .brand{display:flex;align-items:center;gap:8px;color:var(--navy);font-weight:600;line-height:1.05}
  .brand-dot{border-radius:50%;background:var(--navy);flex:none}
  .brand-name{letter-spacing:.06em;text-transform:uppercase;white-space:nowrap}
  .brand-sub{display:block;letter-spacing:.2em;text-transform:uppercase}

  .faint-mark{position:absolute;border-radius:50%;background:var(--faint)}

  /* letterhead */
  .letterhead{left:38px;top:34px;width:514px;height:676px}
  .letterhead .stripe{position:absolute;left:0;top:0;bottom:0;width:10px;background:linear-gradient(180deg,var(--gold-light),var(--gold) 40%,var(--gold-deep))}
  .letterhead .brand{position:absolute;left:30px;top:26px}
  .letterhead .brand-dot{width:26px;height:26px}
  .letterhead .brand-name{font-size:18px}
  .letterhead .brand-sub{font-size:8px;margin-top:3px}
  .letterhead .contact{position:absolute;left:394px;top:28px;font-size:7.5px;line-height:1.45}
  .letterhead .faint-mark{right:36px;bottom:16px;width:180px;height:180px}

  /* business cards */
  .card{top:163px;height:149px;overflow:hidden}
  .card-front{left:619px;width:221px}
  .card-front .stripe{position:absolute;left:0;top:0;bottom:0;width:8px;background:linear-gradient(180deg,var(--gold-light),var(--gold) 50%,var(--gold-deep))}
  .card-front .brand{position:absolute;left:14px;top:38px;flex-direction:column;align-items:center;gap:4px;text-align:center}
  .card-front .brand-dot{width:20px;height:20px}
  .card-front .brand-name{font-size:10px}
  .card-front .brand-sub{font-size:5px;margin-top:2px}
  .card-front .person{position:absolute;left:122px;top:26px}
  .person-name{font-size:10px;font-weight:700;color:var(--navy);white-space:nowrap}
  .person-role{font-size:6.5px;margin-top:1px}
  .person-details{font-size:5.5px;line-height:1.45;margin-top:10px}

  .card-back{left:869px;width:237px}
  .card-back svg{position:absolute;inset:0}
  .card-back .person{position:absolute;left:10px;top:20px;color:#fff}
  .card-back .person-name,.card-back .person-role{color:#fff}
  .card-back .brand{position:absolute;right:12px;top:48px;flex-direction:column;align-items:center;gap:4px;text-align:center}
  .card-back .brand-dot{width:20px;height:20px}
  .card-back .brand-name{font-size:11px}
  .card-back .brand-sub{font-size:5px;margin-top:2px}

  /* envelope */
  .envelope{left:595px;top:365px;width:557px;height:345px;overflow:hidden}
  .envelope svg.flap{position:absolute;left:0;top:0}
  .envelope .brand{position:absolute;left:22px;top:112px;flex-direction:column;align-items:center;gap:5px;text-align:center}
  .envelope .brand-dot{width:28px;height:28px}
  .envelope .brand-name{font-size:20px}
  .envelope .brand-sub{font-size:8px;margin-top:3px}
  .envelope .return{position:absolute;left:22px;top:200px;font-size:8.5px;font-weight:600}
  .envelope .faint-mark{right:12px;bottom:30px;width:100px;height:100px}
</style>
</head>
<body>

<section class="sheet letterhead" aria-label="Letterhead">
  <div class="stripe"></div>
  <div class="brand">
    <span class="brand-dot"></span>
    <span><span class="brand-name">Copperfield</span><span class="brand-sub">Real Estate</span></span>
  </div>
  <address class="contact">
    418 Tamsin Rd<br>Ashbury, PA 19377<br>Phone: 555-201-4480<br>Fax: 555-201-4481<br>www.copperfieldre.com
  </address>
  <div class="faint-mark" aria-hidden="true"></div>
</section>

<section class="sheet card card-front" aria-label="Business card front">
  <div class="stripe"></div>
  <div class="brand">
    <span class="brand-dot"></span>
    <span><span class="brand-name">Copperfield</span><span class="brand-sub">Real Estate</span></span>
  </div>
  <div class="person">
    <div class="person-name">Glen Hartwick Sr.</div>
    <div class="person-role">Managing Partner</div>
    <address class="person-details">
      418 Tamsin Rd<br>Ashbury, PA 19377<br>Phone: 555-201-4480<br>Cell: 555-201-4482<br>Fax: 555-201-4481<br>glen@copperfieldre.com<br>www.copperfieldre.com
    </address>
  </div>
</section>

<section class="sheet card card-back" aria-label="Business card back">
  <svg width="237" height="149" viewBox="0 0 237 149" aria-hidden="true">
    <defs>
      <linearGradient id="cardGold" x1="0" y1="0" x2="1" y2="1">
        <stop offset="0" stop-color="#f9d46a"/>
        <stop offset=".5" stop-color="#f0b323"/>
        <stop offset="1" stop-color="#d9950f"/>
      </linearGradient>
    </defs>
    <path d="M0 0H118C95 37 95 112 118 149H0Z" fill="url(#cardGold)"/>
    <path d="M118 0C95 37 95 112 118 149" fill="none" stroke="#1c2f6b" stroke-width="4"/>
  </svg>
  <div class="person">
    <div class="person-name">Glen Hartwick Sr.</div>
    <div class="person-role">Managing Partner</div>
    <address class="person-details">
      418 Tamsin Rd<br>Ashbury, PA 19377<br>Phone: 555-201-4480<br>Cell: 555-201-4482<br>Fax: 555-201-4481<br>glen@copperfieldre.com<br>www.copperfieldre.com
    </address>
  </div>
  <div class="brand">
    <span class="brand-dot"></span>
    <span><span class="brand-name">Copperfield</span><span class="brand-sub">Real Estate</span></span>
  </div>
</section>

<section class="sheet envelope" aria-label="Envelope">
  <svg class="flap" width="557" height="345" viewBox="0 0 557 345" aria-hidden="true">
    <defs>
      <linearGradient id="flapGold" x1="0" y1="0" x2="0" y2="1">
        <stop offset="0" stop-color="#d9950f"/>
        <stop offset=".6" stop-color="#f0b323"/>
        <stop offset="1" stop-color="#f9d46a"/>
      </linearGradient>
    </defs>
    <path d="M0 0H557V40L290 106H267L0 40Z" fill="url(#flapGold)"/>
  </svg>
  <div class="brand">
    <span class="brand-dot"></span>
    <span><span class="brand-name">Copperfield</span><span class="brand-sub">Real Estate</span></span>
  </div>
  <address class="return">418 Tamsin Rd, Ashbury, PA 19377</address>
  <div class="faint-mark" aria-hidden="true"></div>
</section>

</body>
</html>
```